Skin cancer clinic services trifold brochure

Need trifold brochure listing skin cancer services our clinic provides, staff information, location and brief about skin cancer with colours similar to our web site www.Lumorava.clinic. I will provide more information regarding services and staff but want this colourful and standout as it will be given to other referring doctors or patients

Target Market(s)

Age 40 to 80 years

Industry/Entity Type

Medical

Font styles to use
Serif

Colors

Designer to choose colors to be used in the design.

Requirements
Must have
• Logo, services, contact info, beach or sun look and colours similar to web site or logo

```html
<!DOCTYPE html>
<html lang="en">
<head>
<meta charset="utf-8">
<title>Lumorava Skin Cancer Clinic – Brochure Panel</title>
<link rel="stylesheet" href="https://fonts.googleapis.com/css2?family=Domine:wght@400;700&display=swap">
<style>
  :root{
    --orange:#e8822f;
    --orange-soft:#ef9f5c;
    --orange-mid:#ec8b3a;
    --ink:#262626;
    --text:#2b2b2b;
    --paper-a:#fbeee9;
    --paper-b:#fdf3ea;
    --sea-a:#cfe6f3;
    --sea-b:#6fb0cc;
    --sea-c:#d9c6a6;
  }
  *{box-sizing:border-box;margin:0;padding:0}
  html,body{width:1200px;height:933px;overflow:hidden}
  body{font-family:"Domine",Georgia,serif;color:var(--text)}
  .brochure{position:relative;width:1200px;height:933px;overflow:hidden;
    background:linear-gradient(90deg,var(--paper-a),var(--paper-b))}
  .decor{position:absolute;inset:0}
  .staff{position:absolute;font-size:16.4px;line-height:23.7px}
  .staff h2{color:var(--orange);font-size:19.5px;font-weight:700;line-height:24px;margin-bottom:2px}
  .staff p{margin:0}
  .staff-left{left:25px;top:55px;width:370px}
  .staff-left .member+ .member{margin-top:16px}
  .staff-right{left:428px;top:53px;width:340px}
  .contact{position:absolute;left:430px;top:281px;width:340px;text-align:center;font-size:16.4px}
  .contact-title{display:inline-block;background:var(--orange);color:#fff;font-weight:700;
    font-size:18px;padding:6px 17px 5px;letter-spacing:.3px;margin-left:-30px}
  .contact-line{display:flex;justify-content:center;align-items:center;gap:8px;margin-top:8px;line-height:22px}
  .contact-line svg{flex:none}
  .address{margin-top:10px;align-items:flex-start}
  .email{color:var(--orange)}
  .brand{position:absolute;left:868px;top:70px;width:240px;text-align:center;color:var(--ink);font-weight:700}
  .brand-name{display:flex;align-items:center;justify-content:center;gap:10px;font-size:34px;letter-spacing:1px;line-height:40px}
  .brand-dot{width:26px;height:26px;border-radius:50%;background:var(--orange)}
  .brand-tag{font-size:11.5px;letter-spacing:2.6px;margin-top:4px}
  .headline{position:absolute;right:165px;top:215px;text-align:right;font-weight:700;line-height:1}
  .headline span{display:block}
  .hl-when{color:var(--orange);font-size:59px;letter-spacing:5px}
  .hl-was{color:var(--ink);font-size:38px;font-weight:400;margin-top:0}
  .hl-last{color:var(--orange);font-size:46px;margin-top:0}
  .hl-skin{color:var(--orange);font-size:74px;margin-top:-4px}
  .hl-check{color:var(--ink);font-size:30px;margin-top:-2px;margin-right:16px}
  .qmark{position:absolute;left:1018px;top:168px;font-weight:700;font-size:290px;line-height:1;color:var(--ink);
    text-shadow:8px 8px 0 var(--orange)}
</style>
</head>
<body>
<main class="brochure">
  <svg class="decor" width="1200" height="933" viewBox="0 0 1200 933" aria-hidden="true">
    <polygon points="0,793 118,676 375,933 0,933" fill="var(--orange-soft)"/>
    <polygon points="615,449 880,714 615,979 350,714" fill="none" stroke="var(--ink)" stroke-width="1.2"/>
    <polygon points="980,449 1245,714 980,979 715,714" fill="none" stroke="var(--ink)" stroke-width="1.2"/>
    <polygon points="497,522 690,714 497,906 304,714" fill="var(--orange-mid)"/>
    <polygon points="1101,522 1293,714 1101,906 909,714" fill="var(--orange-mid)"/>
    <polygon points="466,521 659,714 466,907 273,714" fill="none" stroke="var(--ink)" stroke-width="5"/>
    <polygon points="1126,521 1319,714 1126,907 933,714" fill="none" stroke="var(--ink)" stroke-width="5"/>
    <polygon points="791,370 873,450 791,530 709,450" fill="none" stroke="var(--ink)" stroke-width="6"/>
    <polygon points="794,408 1102,714 794,1020 486,714" fill="#fff"/>
    <polygon points="794,418 1093,714 794,1010 497,714" fill="var(--orange)"/>
    <polygon points="712,832 794,914 876,832 794,750" fill="none" stroke="var(--ink)" stroke-width="6" transform="translate(0,80)"/>
  </svg>
  <svg class="decor" width="1200" height="933" viewBox="0 0 1200 933" role="img" aria-label="Photo of a small child in a duck swim vest splashing in shallow sea water at the beach">
    <defs>
      <linearGradient id="seaGradient" x1="0" y1="0" x2="0" y2="1">
        <stop offset="0" stop-color="var(--sea-a)"/>
        <stop offset=".55" stop-color="var(--sea-b)"/>
        <stop offset="1" stop-color="var(--sea-c)"/>
      </linearGradient>
    </defs>
    <polygon points="794,450 1066,717 794,985 527,717" fill="url(#seaGradient)"/>
  </svg>

  <section class="staff staff-left">
    <article class="member">
      <h2>Dr. Maren Colvey:</h2>
      <p>BMed. FRACGP. Diploma Skin Cancer --<br>Medicine/Surgery.<br>Born in Australia.<br>Dr. Colvey enjoys the Outdoors, Gardening,<br>Family, Beach, and Holidays.<br>Professional interests include Skin Care &amp;<br>Cosmetic Treatments, Family Medicine.</p>
    </article>
    <article class="member">
      <h2>Dr. Hollis Brandt:</h2>
      <p>MBBS.<br>Born in the USA and moved to Australia in<br>2004.<br>Hollis completed her Medical Degree at<br>Harbourview University. NSW. In 2004.<br>Dr. Brandt enjoys Running, Fitness,<br>Spending quality time with family and<br>visiting the beach.<br>Professional interests include Skin Care,<br>Cosmetic Treatments and Family Medicine.</p>
    </article>
    <article class="member">
      <h2>Tessa Wyland:</h2>
      <p>Registered Nurse:<br>Tessa is our Laser Treatment Specialist and<br>is available via appointment</p>
    </article>
  </section>

  <section class="staff staff-right">
    <article class="member">
      <h2>Ilsa Renwick:</h2>
      <p>Registered Nurse:<br>AINEM Certificate in Nutritional and<br>Environmental Medicine<br>Medi Cosmetic Nurse:<br>Ilsa is our Cosmetic Specialist and is<br>available by appointment.</p>
    </article>
  </section>

  <section class="contact">
    <h3 class="contact-title">CONTACT US</h3>
    <div class="contact-line address">
      <svg width="18" height="22" viewBox="0 0 18 22"><path d="M9 0a8 8 0 0 0-8 8c0 6 8 14 8 14s8-8 8-14a8 8 0 0 0-8-8zm0 11a3 3 0 1 1 0-6 3 3 0 0 1 0 6z" fill="var(--orange)"/></svg>
      <span>Suites 1 &amp; 2 316 Coral Parade<br>Eastbrook NSW 2260</span>
    </div>
    <div class="contact-line">
      <svg width="24" height="24" viewBox="0 0 24 24"><circle cx="12" cy="12" r="12" fill="var(--orange)"/><path d="M8 6l2.5 3-1.3 1.5c.8 1.8 2.3 3.3 4.2 4.2L15 13.5l3 2.5-1.5 2.2c-5 .2-10.5-5.3-10.3-10.3z" fill="#fff"/></svg>
      <span>1300 555 018</span>
    </div>
    <div class="contact-line email">
      <svg width="20" height="16" viewBox="0 0 20 16"><path d="M0 5l10-5 10 5v11H0z" fill="var(--orange)"/><path d="M2 5l8 5 8-5" fill="none" stroke="#fff" stroke-width="1.6"/></svg>
      <span>admin@lumorava.clinic</span>
    </div>
  </section>

  <header class="brand">
    <div class="brand-name"><span class="brand-dot"></span><span>LUMORAVA</span></div>
    <div class="brand-tag">SKIN CANCER CLINIC</div>
  </header>

  <h1 class="headline">
    <span class="hl-when">WHEN</span>
    <span class="hl-was">WAS YOUR</span>
    <span class="hl-last">LAST</span>
    <span class="hl-skin">SKIN</span>
    <span class="hl-check">CHECK</span>
  </h1>
  <div class="qmark" aria-hidden="true">?</div>
</main>
</body>
</html>
```